Online Psychology Practice needs business cards.

Online Psychology service needs business cards. Have own logo- please see uploaded. I have other file formats if you need (not sure one needed?)

Details for Business Card:
Fiona Kettlewood
Clinical Psychologist BPsych, BPsych (Hons), MPsych (Clin), MAPS
T: 0457260714 | F: 08 71526804
E: hello@harbourlightmindcarestudio.com.au
W: harbourlightmindcarestudio.com.au

Industry/Entity Type

Health

Contact Information for Business Card

Logo plus details above (couldn't write in this section)

```html
<!DOCTYPE html>
<html lang="en">
<head>
<meta charset="UTF-8">
<title>Harbourlight Mindcare Studio — Business Cards</title>
<link rel="stylesheet" href="https://fonts.googleapis.com/css2?family=Cormorant+Garamond:ital,wght@0,600;1,500&family=Roboto:wght@400&display=swap">
<style>
  :root {
    --backdrop: #6b6868;
    --card-blue-light: #1b7396;
    --card-blue-dark: #1e4c78;
    --paper: #f3f3f4;
    --ink: #2a2a2e;
    --navy: #1d3f6e;
    --teal: #1f7ea3;
    --white: #ffffff;
  }
  * { box-sizing: border-box; margin: 0; padding: 0; }
  html, body {
    width: 1200px;
    height: 1200px;
    overflow: hidden;
    background: var(--backdrop);
  }
  .stage {
    position: relative;
    width: 1200px;
    height: 1200px;
  }
  .card {
    position: absolute;
    left: 300px;
    width: 594px;
    height: 350px;
    border-radius: 20px;
    overflow: hidden;
  }
  /* Front */
  .card-front {
    top: 200px;
    background: linear-gradient(135deg, var(--card-blue-light) 0%, var(--card-blue-dark) 100%);
    color: var(--white);
  }
  .front-brand {
    position: absolute;
    top: 118px;
    left: 0;
    width: 100%;
    text-align: center;
    font-family: "Cormorant Garamond", serif;
    font-weight: 600;
    font-size: 44px;
    line-height: 1.02;
    letter-spacing: 2px;
    text-transform: uppercase;
    color: var(--white);
  }
  .front-web {
    position: absolute;
    bottom: 28px;
    left: 0;
    width: 100%;
    text-align: center;
    font-family: "Roboto", sans-serif;
    font-size: 15.5px;
    color: var(--white);
  }
  /* Back */
  .card-back {
    top: 640px;
    background: var(--paper);
    color: var(--ink);
  }
  .person {
    position: absolute;
    left: 40px;
    top: 58px;
  }
  .person-name {
    font-family: "Cormorant Garamond", serif;
    font-weight: 600;
    font-size: 25px;
    letter-spacing: 1px;
    text-transform: uppercase;
    color: var(--ink);
  }
  .person-role {
    font-family: "Cormorant Garamond", serif;
    font-style: italic;
    font-weight: 500;
    font-size: 18px;
    color: var(--teal);
    margin-top: 2px;
  }
  .person-credentials {
    font-family: "Roboto", sans-serif;
    font-size: 13.5px;
    line-height: 18px;
    color: var(--ink);
    margin-top: 6px;
  }
  .back-brand {
    position: absolute;
    left: 335px;
    top: 72px;
    width: 230px;
    text-align: center;
  }
  .brand-dot {
    display: block;
    width: 58px;
    height: 58px;
    margin: 0 auto 16px;
    border-radius: 50%;
    background: var(--teal);
  }
  .brand-name {
    font-family: "Cormorant Garamond", serif;
    font-weight: 600;
    font-size: 26px;
    line-height: 1.05;
    letter-spacing: 1px;
    text-transform: uppercase;
    color: var(--navy);
  }
  .contacts {
    position: absolute;
    left: 40px;
    top: 236px;
    list-style: none;
    font-family: "Roboto", sans-serif;
    font-size: 14px;
    color: var(--ink);
  }
  .contacts li {
    display: flex;
    align-items: center;
    height: 20px;
  }
  .contacts svg {
    width: 13px;
    height: 13px;
    margin-right: 10px;
    fill: var(--navy);
    flex: none;
  }
  .web-accent { color: var(--teal); }
</style>
</head>
<body>
<main class="stage">
  <section class="card card-front" aria-label="Business card front">
    <div class="front-brand">Harbourlight<br>Mindcare Studio</div>
    <p class="front-web">www.harbourlightmindcarestudio.com.au</p>
  </section>

  <section class="card card-back" aria-label="Business card back">
    <div class="person">
      <h1 class="person-name">Fiona Kettlewood</h1>
      <p class="person-role">Clinical Psychologist</p>
      <p class="person-credentials">BPsych, BPsych (Hons),<br>MPsych (Clin), MAPS</p>
    </div>

    <div class="back-brand">
      <span class="brand-dot"></span>
      <div class="brand-name">Harbourlight<br>Mindcare Studio</div>
    </div>

    <ul class="contacts">
      <li>
        <svg viewBox="0 0 16 16" aria-hidden="true"><path d="M2 5c0-2 2-3 6-3s6 1 6 3v1h-3V5H5v1H2z M4 7h8l2 6H2z"/></svg>
        04 57260714
      </li>
      <li>
        <svg viewBox="0 0 16 16" aria-hidden="true"><path d="M4 1h8v4H4z M1 6h14v6h-3v3H4v-3H1z M5 10v4h6v-4z"/></svg>
        08 71526804
      </li>
      <li>
        <svg viewBox="0 0 16 16" aria-hidden="true"><path d="M1 3h14v10H1z M2 4l6 5 6-5v1L8 10 2 5z" fill-rule="evenodd"/></svg>
        hello@harbourlightmindcarestudio.com.au
      </li>
      <li>
        <svg viewBox="0 0 16 16" aria-hidden="true"><path d="M8 1a7 7 0 1 0 0 14A7 7 0 0 0 8 1zm0 1.5c.8 0 1.7 1.6 2 4H6c.3-2.4 1.2-4 2-4zM2.6 6.5h2.2c0-1.3.3-2.6.7-3.5a5.5 5.5 0 0 0-2.9 3.5zm8.6 0h2.2a5.5 5.5 0 0 0-2.9-3.5c.4.9.7 2.2.7 3.5zM2.6 9.5a5.5 5.5 0 0 0 2.9 3.5c-.4-.9-.7-2.2-.7-3.5zm3.4 0c.3 2.4 1.2 4 2 4s1.7-1.6 2-4zm5.2 0c0 1.3-.3 2.6-.7 3.5a5.5 5.5 0 0 0 2.9-3.5z"/></svg>
        www.harbourlight<span class="web-accent">mindcare</span>studio.com.au
      </li>
    </ul>
  </section>
</main>
</body>
</html>
```